Need Letterhead and Business Card

I have a logo but i need new letterhead and biz cards. We are a real estate investment firm so we need very professional but also do not want to be old fashioned. We have 3 locations; Singapore, New York and Ponte Vedra Florida. I can provide full addresses if needed. If you have adjustments to our logo you would recommend we are open to them.
I will be putting in a separate project but we also need a template for our own powerpoint slide presentations and website.

Industry/Entity Type

Real Estate

```html
<!DOCTYPE html>
<html lang="en">
<head>
<meta charset="utf-8">
<title>Kestrel Stationery – Letterhead and Business Cards</title>
<link href="https://fonts.googleapis.com/css2?family=Open+Sans:wght@400;600;700&display=swap" rel="stylesheet">
<style>
  :root{
    --brand-blue:#1d5a8e;
    --brand-gold:#c9a04a;
    --ink:#2a2a2a;
    --paper:#ffffff;
    --backdrop:#eeeff1;
  }
  *{box-sizing:border-box;margin:0;padding:0}
  html,body{width:1200px;height:795px;overflow:hidden}
  body{background:var(--backdrop);font-family:"Open Sans",Arial,sans-serif;color:var(--ink);position:relative}

  /* Letterhead */
  .letterhead{position:absolute;left:60px;top:26px;width:524px;height:742px;background:var(--paper);
    box-shadow:0 2px 10px rgba(0,0,0,.12)}
  .letterhead .band-top{position:absolute;left:0;right:0;top:0;height:16px;background:var(--brand-blue)}
  .letterhead .band-bottom{position:absolute;left:0;right:0;bottom:0;height:14px;background:var(--brand-blue)}
  .letterhead .header{position:absolute;left:34px;right:34px;top:48px;display:flex;align-items:flex-start}
  .brand{display:flex;flex-direction:column}
  .brand-name{font-weight:700;color:var(--brand-blue);letter-spacing:1px;line-height:1}
  .brand-tag{color:var(--brand-gold);text-transform:uppercase;letter-spacing:.4px;margin-top:3px}
  .letterhead .brand-name{font-size:26px}
  .letterhead .brand-tag{font-size:5.5px}
  .offices{display:flex;margin-left:auto;gap:44px}
  .office{font-size:9px;line-height:1.3;color:var(--brand-blue)}
  .letterhead .body{position:absolute;left:52px;right:46px;top:190px;font-size:9.6px;line-height:1.75}
  .letterhead .body p + p{margin-top:14px}

  /* Business cards */
  .card{position:absolute;width:350px;height:200px;background:var(--paper);box-shadow:0 2px 10px rgba(0,0,0,.12)}
  .card .band-bottom{position:absolute;left:0;right:0;bottom:0;height:12px;background:var(--brand-blue)}
  .card-front{left:700px;top:150px}
  .card-back{left:700px;top:430px}
  .card-front .brand{position:absolute;left:26px;top:66px}
  .card-front .brand-name{font-size:20px}
  .card-front .brand-tag{font-size:4.6px}
  .person{position:absolute;right:26px;top:26px;text-align:right}
  .person-name{font-size:15px;font-weight:700;color:var(--brand-blue)}
  .person-title{font-size:7.5px;color:var(--brand-gold)}
  .contact{position:absolute;top:136px;font-size:7.5px;line-height:1.45;color:var(--brand-blue)}
  .contact.phones{left:26px}
  .contact.web{left:170px}
  .contact .label{color:var(--brand-gold);margin-right:3px}
  .card-back .locations{position:absolute;left:26px;right:26px;top:76px}
  .locations-title{font-size:8.5px;color:var(--brand-gold);margin-bottom:8px}
  .card-back .offices{margin-left:0;gap:30px}
  .card-back .office{font-size:7px}
</style>
</head>
<body>

<section class="letterhead">
  <div class="band-top"></div>
  <header class="header">
    <div class="brand">
      <span class="brand-name">KESTREL</span>
      <span class="brand-tag">Real Estate Investment &amp; Management</span>
    </div>
    <div class="offices">
      <p class="office">28 Linden Crescent<br>Singapore 248571</p>
      <p class="office">560 Harbor Street<br>NY NY 10016</p>
      <p class="office">145 Coastal Way<br>Suite 220<br>Ponte Vedra, Fl 32081</p>
    </div>
  </header>
  <div class="body">
    <p>Lorem ipsum dolor sit amet, consectetur adipiscing elit. Nulla fringilla, massa vel fermentum pellentesque, elit turpis varius urna, sit amet sagittis libero enim et nisl. Cras justo turpis, imperdiet ut sem suscipit, volutpat feugiat mi. Sed lobortis placerat libero, a gravida urna maximus nec. Integer id pretium ex, ultrices pulvinar lorem. Donec leo enim, tincidunt vitae neque ut, elementum viverra justo. In eget augue vitae sapien gravida aliquet id eu elit. Vestibulum iaculis posuere nulla. Suspendisse ultricies mauris viverra nisi finibus, eget faucibus diam pulvinar. Vestibulum in consectetur mi. Nulla facilisi. Phasellus bibendum augue sed est ornare, sit amet fringilla magna lacinia. Nam nec tellus eget tellus maximus scelerisque quis ac mi. Nullam quis elementum ex. Aenean feugiat, ultrices felis, a euismod lectus vestibulum sit amet. Aliquam semper gravida porttitor. Fusce sed fermentum mauris.</p>
    <p>In est sapien, scelerisque nec cursus sed, bibendum eget metus. Donec et orci nulla. Nunc eleifend, erat ut imperdiet condimentum, ipsum augue dictum neque, ut elementum velit dolor eu ex. Nullam maximus ligula vel purus tempus semper. Curabitur in est blandit leo eleifend pharetra. Quisque ultrices dictum erat eget scelerisque. Phasellus aliquam justo eget lacinia mollis.</p>
  </div>
  <div class="band-bottom"></div>
</section>

<section class="card card-front">
  <div class="person">
    <p class="person-name">Daniel Reyes</p>
    <p class="person-title">Managing Director</p>
  </div>
  <div class="brand">
    <span class="brand-name">KESTREL</span>
    <span class="brand-tag">Real Estate Investment &amp; Management</span>
  </div>
  <p class="contact phones"><span class="label">P</span>000.000.0000<br><span class="label">F</span>000.000.0000</p>
  <p class="contact web">hello@kestrelre.com<br>kestrelre.com</p>
  <div class="band-bottom"></div>
</section>

<section class="card card-back">
  <div class="locations">
    <p class="locations-title">Our Locations</p>
    <div class="offices">
      <p class="office">28 Linden Crescent<br>Singapore 248571</p>
      <p class="office">560 Harbor Street<br>NY NY 10016</p>
      <p class="office">145 Coastal Way<br>Suite 220<br>Ponte Vedra, Fl 32081</p>
    </div>
  </div>
  <div class="band-bottom"></div>
</section>

</body>
</html>
```